Custom website design and development needed for Davrune , a music and video streaming and download w

Organization or website name
Davrune
Navigation
Artist listing
Top 20 artists
Top 20 songs
Top 20 videos

We are looking to build a website that will allow customers who are music lovers to search,play online or download music or video of their choice as people all around the globe have got a strong fondness for music and the popularity of various singers and musicians proves this point.It should be eye catching and easily navigatable with a nice clean look and feel to it.
Nice to have
Simple logo
Alphabetical sorting of songs by artist
Content Area should contain 3 columns
Top 20 artists
Top 20 songs
Top 20 videos
We need functionality to browse from A to Z in Artist name and music title and search all mp3 in the data base.

Some examples for reference are:

http://tunecrate.example/

https://melovantis.example/

Industry/Entity Type

Artists

Coding

Coded - Design and coding required

```html
<!DOCTYPE html>
<html lang="en">
<head>
<meta charset="utf-8">
<title>Davrune — Music and Video Streaming</title>
<link rel="stylesheet" href="https://fonts.googleapis.com/css2?family=Amaranth:wght@400;700&family=Fira+Sans:wght@400;500;600;800&display=swap">
<style>
  :root {
    --yellow: #f7c510;
    --brown: #4a1c0f;
    --cream: #fcecc4;
    --white: #ffffff;
    --ink: #2b2b2b;
    --dark: #0b1a24;
    --line: #d9d9d9;
  }
  * { margin: 0; padding: 0; box-sizing: border-box; }
  html, body { width: 1058px; height: 1200px; overflow: hidden; }
  body {
    position: relative;
    background: var(--cream);
    font-family: "Fira Sans", sans-serif;
    color: var(--ink);
  }
  a { text-decoration: none; color: inherit; }

  /* Header */
  .site-header {
    position: absolute; left: 0; top: 0; width: 1058px; height: 187px;
    border-top: 3px solid var(--yellow);
  }
  .header-backdrop {
    position: absolute; inset: 0;
    background:
      radial-gradient(ellipse at 62% 70%, rgba(120,60,80,.55), transparent 55%),
      radial-gradient(ellipse at 20% 40%, rgba(60,40,90,.5), transparent 60%),
      linear-gradient(100deg, #222 0%, #3a3340 45%, #2c3a2a 75%, #1d1d1d 100%);
  }
  .brand-mark {
    position: absolute; left: 262px; top: 38px; width: 92px; height: 92px;
    border-radius: 50%; background: var(--yellow);
  }
  .brand-name {
    position: absolute; left: 397px; top: 28px;
    font-family: "Fira Sans", sans-serif; font-weight: 800; font-size: 44px;
    color: var(--yellow); letter-spacing: 1px;
  }
  .search {
    position: absolute; left: 397px; top: 102px; width: 407px; height: 32px;
    display: flex; background: var(--white);
  }
  .search-input {
    flex: 1; border: 0; padding-left: 10px; font-family: "Amaranth", sans-serif;
    font-size: 14px; font-weight: 700; color: #666; letter-spacing: .5px;
    display: flex; align-items: center;
  }
  .search-button {
    width: 39px; border-left: 2px solid var(--yellow);
    display: flex; align-items: center; justify-content: center;
  }
  .search-scope {
    position: absolute; top: 146px; left: 399px; display: flex;
    font-family: "Amaranth", sans-serif; font-weight: 700; font-size: 14px; color: var(--white);
  }
  .scope-option { display: flex; align-items: center; gap: 4px; margin-right: 36px; letter-spacing: .5px; }
  .scope-dot { width: 9px; height: 9px; border-radius: 50%; background: var(--white); }
  .scope-dot.is-selected { background: transparent; border: 2px solid var(--white); }

  /* Navigation */
  .main-nav {
    position: absolute; left: 0; top: 187px; width: 1058px; height: 32px;
    background: var(--brown); display: flex; align-items: center;
    font-family: "Fira Sans", sans-serif; font-weight: 500; font-size: 13px; letter-spacing: .6px;
  }
  .nav-link { color: var(--yellow); position: absolute; }
  .artist-listing { position: absolute; left: 541px; color: var(--white); display: flex; gap: 4px; }
  .artist-listing .letters { margin-left: 6px; font-size: 11.5px; letter-spacing: 1.9px; padding-top: 1px; }

  /* Content panel */
  .content {
    position: absolute; left: 87px; top: 219px; width: 884px; height: 929px;
    background: var(--white);
    border-left: 1px solid #cfcfcf; border-right: 1px solid #cfcfcf;
  }
  .charts { position: absolute; left: 23px; top: 34px; display: flex; gap: 22px; }
  .chart { width: 264px; }
  .chart-title {
    height: 33px; background: var(--yellow); color: var(--white);
    font-weight: 500; font-size: 18px; letter-spacing: 1px;
    display: flex; align-items: center; justify-content: center;
  }
  .chart-list { list-style: none; margin-top: 4px; display: grid; grid-template-columns: 128px 128px; column-gap: 8px; row-gap: 4px; }
  .chart-item {
    height: 26.4px; border: 1px solid var(--yellow);
    display: flex; align-items: center; padding-left: 8px; gap: 5px;
    font-size: 12px; color: #333;
  }
  .chart-item svg { width: 10px; height: 12px; flex: none; }
  .divider { position: absolute; left: 0; top: 398px; width: 884px; height: 1px; background: var(--line); }

  /* App promo */
  .app-phone {
    position: absolute; left: 99px; top: 421px; width: 130px; height: 230px;
    border: 2px solid #8a6a6a; border-radius: 12px;
    background: linear-gradient(180deg, #eaf6fb 0%, #eef3ea 40%, #fbe8e0 70%, #eef4fb 100%);
  }
  .app-promo { position: absolute; left: 300px; top: 466px; width: 430px; text-align: center; font-family: "Amaranth", sans-serif; color: var(--brown); }
  .app-title { font-size: 24px; font-weight: 400; letter-spacing: 1px; }
  .app-tagline { margin-top: 8px; font-size: 13px; font-weight: 700; letter-spacing: .7px; }
  .store-links { margin-top: 22px; display: flex; justify-content: center; gap: 11px; }
  .store-badge {
    height: 31px; background: #111; border: 1px solid #888; border-radius: 4px;
    color: var(--white); font-family: "Fira Sans", sans-serif; font-size: 14px;
    display: flex; align-items: center; gap: 6px; padding: 0 9px;
  }
  .store-badge .badge-dot { width: 10px; height: 10px; background: var(--white); border-radius: 2px; }

  /* Streaming banner */
  .stream-banner {
    position: absolute; left: 0; top: 652px; width: 882px; height: 183px;
    background:
      radial-gradient(ellipse at 74% 55%, rgba(170,160,150,.45), transparent 35%),
      radial-gradient(ellipse at 88% 30%, rgba(90,110,130,.5), transparent 40%),
      linear-gradient(90deg, var(--dark) 0%, var(--dark) 55%, #1d2c36 100%);
  }
  .stream-title {
    position: absolute; left: 96px; top: 44px; color: var(--white);
    font-family: "Amaranth", sans-serif; font-size: 28px; letter-spacing: 1.5px;
  }
  .download-button {
    position: absolute; left: 178px; top: 92px; width: 172px; height: 35px;
    background: var(--yellow); border-radius: 2px; color: var(--brown);
    font-family: "Amaranth", sans-serif; font-weight: 700; font-size: 27px; letter-spacing: 1.5px;
    display: flex; align-items: center; justify-content: center;
  }
  .sign-off {
    position: absolute; left: 0; top: 864px; width: 882px; text-align: center;
    font-family: "Amaranth", sans-serif; font-weight: 700; font-size: 29px; color: var(--brown); letter-spacing: 1.2px;
  }

  /* Footer */
  .site-footer {
    position: absolute; left: 0; top: 1148px; width: 1058px; height: 52px;
    background: var(--yellow); display: flex; align-items: center; justify-content: center;
    font-size: 10px; color: #3a2a10; letter-spacing: .4px; padding-bottom: 8px;
  }
</style>
</head>
<body>
<svg width="0" height="0" style="position:absolute">
  <symbol id="note" viewBox="0 0 10 12">
    <path d="M4 0h1.6c.3 1.6 1.6 2.4 3 3.2L8 4.4C7 3.9 6.2 3.4 5.6 2.7V9.5C5.6 11 4.3 12 2.8 12 1.2 12 0 11.2 0 10s1.3-2 2.7-2c.5 0 .9.1 1.3.3V0z" fill="#222"/>
  </symbol>
</svg>

<header class="site-header">
  <div class="header-backdrop" role="img" aria-label="Dark photograph of piano keys with colourful floating music notes"></div>
  <div class="brand-mark"></div>
  <div class="brand-name">Davrune</div>
  <div class="search">
    <div class="search-input">Search here...</div>
    <div class="search-button">
      <svg width="20" height="20" viewBox="0 0 20 20"><circle cx="8.5" cy="8.5" r="6.5" fill="none" stroke="#f7c510" stroke-width="2.4"/><path d="M13.3 13.3 18.5 18.5" stroke="#f7c510" stroke-width="2.6" stroke-linecap="round"/></svg>
    </div>
  </div>
  <div class="search-scope">
    <span class="scope-option"><span class="scope-dot is-selected"></span>All</span>
    <span class="scope-option"><span class="scope-dot"></span>Song</span>
    <span class="scope-option"><span class="scope-dot"></span>Artist</span>
  </div>
</header>

<nav class="main-nav">
  <a class="nav-link" style="left:111px" href="#">Top 20 Artists</a>
  <a class="nav-link" style="left:235px" href="#">Top 20 Songs</a>
  <a class="nav-link" style="left:351px" href="#">Top 20 Videos</a>
  <div class="artist-listing"><span>Artist Listing:</span><span class="letters">A B C D E F G H I J K L M N O P Q R S T U V W X Y Z</span></div>
</nav>

<main class="content">
  <div class="charts">
    <section class="chart">
      <h2 class="chart-title">Top 20 Artists</h2>
      <ul class="chart-list">
        <li class="chart-item"><svg><use href="#note"/></svg>Artists Songs</li><li class="chart-item"><svg><use href="#note"/></svg>Artists Songs</li>
        <li class="chart-item"><svg><use href="#note"/></svg>Artists Songs</li><li class="chart-item"><svg><use href="#note"/></svg>Artists Songs</li>
        <li class="chart-item"><svg><use href="#note"/></svg>Artists Songs</li><li class="chart-item"><svg><use href="#note"/></svg>Artists Songs</li>
        <li class="chart-item"><svg><use href="#note"/></svg>Artists Songs</li><li class="chart-item"><svg><use href="#note"/></svg>Artists Songs</li>
        <li class="chart-item"><svg><use href="#note"/></svg>Artists Songs</li><li class="chart-item"><svg><use href="#note"/></svg>Artists Songs</li>
        <li class="chart-item"><svg><use href="#note"/></svg>Artists Songs</li><li class="chart-item"><svg><use href="#note"/></svg>Artists Songs</li>
        <li class="chart-item"><svg><use href="#note"/></svg>Artists Songs</li><li class="chart-item"><svg><use href="#note"/></svg>Artists Songs</li>
        <li class="chart-item"><svg><use href="#note"/></svg>Artists Songs</li><li class="chart-item"><svg><use href="#note"/></svg>Artists Songs</li>
        <li class="chart-item"><svg><use href="#note"/></svg>Artists Songs</li><li class="chart-item"><svg><use href="#note"/></svg>Artists Songs</li>
        <li class="chart-item"><svg><use href="#note"/></svg>Artists Songs</li><li class="chart-item"><svg><use href="#note"/></svg>Artists Songs</li>
      </ul>
    </section>
    <section class="chart">
      <h2 class="chart-title">Top 20 Songs</h2>
      <ul class="chart-list">
        <li class="chart-item"><svg><use href="#note"/></svg>Artists Songs</li><li class="chart-item"><svg><use href="#note"/></svg>Artists Songs</li>
        <li class="chart-item"><svg><use href="#note"/></svg>Artists Songs</li><li class="chart-item"><svg><use href="#note"/></svg>Artists Songs</li>
        <li class="chart-item"><svg><use href="#note"/></svg>Artists Songs</li><li class="chart-item"><svg><use href="#note"/></svg>Artists Songs</li>
        <li class="chart-item"><svg><use href="#note"/></svg>Artists Songs</li><li class="chart-item"><svg><use href="#note"/></svg>Artists Songs</li>
        <li class="chart-item"><svg><use href="#note"/></svg>Artists Songs</li><li class="chart-item"><svg><use href="#note"/></svg>Artists Songs</li>
        <li class="chart-item"><svg><use href="#note"/></svg>Artists Songs</li><li class="chart-item"><svg><use href="#note"/></svg>Artists Songs</li>
        <li class="chart-item"><svg><use href="#note"/></svg>Artists Songs</li><li class="chart-item"><svg><use href="#note"/></svg>Artists Songs</li>
        <li class="chart-item"><svg><use href="#note"/></svg>Artists Songs</li><li class="chart-item"><svg><use href="#note"/></svg>Artists Songs</li>
        <li class="chart-item"><svg><use href="#note"/></svg>Artists Songs</li><li class="chart-item"><svg><use href="#note"/></svg>Artists Songs</li>
        <li class="chart-item"><svg><use href="#note"/></svg>Artists Songs</li><li class="chart-item"><svg><use href="#note"/></svg>Artists Songs</li>
      </ul>
    </section>
    <section class="chart">
      <h2 class="chart-title">Top 20 Videos</h2>
      <ul class="chart-list">
        <li class="chart-item"><svg><use href="#note"/></svg>Video Song</li><li class="chart-item"><svg><use href="#note"/></svg>Video Song</li>
        <li class="chart-item"><svg><use href="#note"/></svg>Video Song</li><li class="chart-item"><svg><use href="#note"/></svg>Video Song</li>
        <li class="chart-item"><svg><use href="#note"/></svg>Video Song</li><li class="chart-item"><svg><use href="#note"/></svg>Video Song</li>
        <li class="chart-item"><svg><use href="#note"/></svg>Video Song</li><li class="chart-item"><svg><use href="#note"/></svg>Video Song</li>
        <li class="chart-item"><svg><use href="#note"/></svg>Video Song</li><li class="chart-item"><svg><use href="#note"/></svg>Video Song</li>
        <li class="chart-item"><svg><use href="#note"/></svg>Video Song</li><li class="chart-item"><svg><use href="#note"/></svg>Video Song</li>
        <li class="chart-item"><svg><use href="#note"/></svg>Video Song</li><li class="chart-item"><svg><use href="#note"/></svg>Video Song</li>
        <li class="chart-item"><svg><use href="#note"/></svg>Video Song</li><li class="chart-item"><svg><use href="#note"/></svg>Video Song</li>
        <li class="chart-item"><svg><use href="#note"/></svg>Video Song</li><li class="chart-item"><svg><use href="#note"/></svg>Video Song</li>
        <li class="chart-item"><svg><use href="#note"/></svg>Video Song</li><li class="chart-item"><svg><use href="#note"/></svg>Video Song</li>
      </ul>
    </section>
  </div>

  <div class="divider"></div>

  <div class="app-phone" role="img" aria-label="Illustration of a smartphone showing a music app store screen"></div>
  <section class="app-promo">
    <h2 class="app-title">Get the app</h2>
    <p class="app-tagline">Never stop listening. Take your playlists and likes wherever you go.</p>
    <div class="store-links">
      <a class="store-badge" href="#"><span class="badge-dot"></span>Tunestore</a>
      <a class="store-badge" href="#"><span class="badge-dot"></span>Playgrid</a>
    </div>
  </section>

  <section class="stream-banner" role="img" aria-label="Dark photograph of a guitarist playing an electric guitar">
    <h2 class="stream-title">Music and Video Streaming</h2>
    <a class="download-button" href="#">Download</a>
  </section>

  <p class="sign-off">Thanks for listening.</p>
</main>

<footer class="site-footer">© 2016 Davrune All Rights Reserved.</footer>
</body>
</html>
```